Valentines Day Helicopter Tour Mailer

The purpose behind this project is to design a mailer for helicopter tours around valentines day. Not sure exaclty all what to include as i'm not sure if i want to price on it yet but i want helicopters, hearts, and something interesting to draw attention to the service we will be offering. If we did include price it would be $169/ person. Size should be good for 8.5 by 11 paper

Target Market(s)

general public

```html
<!DOCTYPE html>
<html lang="en">
<head>
<meta charset="utf-8">
<title>Valentine's Day Helicopter Tour Mailer</title>
<link rel="stylesheet" href="https://fonts.googleapis.com/css2?family=Oswald:wght@500;600&family=Marcellus&family=Allura&display=swap">
<style>
  :root {
    --backdrop: #9b2490;
    --pink: #ec0f8c;
    --magenta: #b0127a;
    --ink: #141414;
    --white: #ffffff;
    --sky: #f6f8f8;
    --horizon: #c9cdd0;
    --tarmac: #5a6270;
    --tarmac-dark: #3d4654;
  }
  * { margin: 0; padding: 0; box-sizing: border-box; }
  html, body {
    width: 1200px;
    height: 2775px;
    overflow: hidden;
    background: var(--backdrop);
  }
  .mailer {
    position: absolute;
    left: 100px;
    top: 745px;
    width: 1000px;
    height: 1284px;
    overflow: hidden;
    background: var(--sky);
  }
  .hero-photo {
    position: absolute;
    inset: 0;
    background: linear-gradient(180deg, var(--sky) 0%, var(--sky) 24%, #eef0f0 33%, var(--horizon) 37%, #8a919a 40%, var(--tarmac) 52%, var(--tarmac) 75%, var(--tarmac-dark) 100%);
  }
  .brand {
    position: absolute;
    top: 72px;
    left: 0;
    width: 100%;
    display: flex;
    justify-content: center;
    align-items: center;
    gap: 14px;
  }
  .brand-mark {
    width: 26px;
    height: 26px;
    background: var(--pink);
  }
  .brand-name {
    font-family: "Oswald", sans-serif;
    font-weight: 600;
    font-size: 48px;
    letter-spacing: 1px;
    color: var(--ink);
    line-height: 1;
  }
  .heart-art {
    position: absolute;
    inset: 0;
    width: 1000px;
    height: 1284px;
  }
  .offer {
    position: absolute;
    left: 352px;
    top: 652px;
    width: 340px;
    text-align: center;
    font-family: "Oswald", sans-serif;
    font-weight: 500;
    color: var(--white);
    text-transform: uppercase;
  }
  .offer-line {
    display: block;
    font-size: 33px;
    line-height: 37px;
  }
  .offer-highlight {
    display: inline-block;
    background: var(--pink);
    border-radius: 20px;
    padding: 0 18px;
    line-height: 35px;
  }
  .offer-sub {
    display: block;
    font-size: 23px;
    line-height: 25px;
    margin-top: 22px;
  }
  .tour-title {
    position: absolute;
    top: 1008px;
    left: 0;
    width: 100%;
    text-align: center;
    font-family: "Allura", cursive;
    font-weight: 400;
    font-size: 124px;
    color: var(--pink);
    line-height: 1;
  }
  .tour-dates {
    position: absolute;
    top: 1146px;
    left: 0;
    width: 100%;
    text-align: center;
    font-family: "Marcellus", serif;
    font-size: 51px;
    color: var(--white);
    line-height: 1;
  }
  .tour-price {
    position: absolute;
    top: 1213px;
    left: 0;
    width: 100%;
    text-align: center;
    font-family: "Marcellus", serif;
    font-size: 38px;
    letter-spacing: 2px;
    color: var(--white);
    line-height: 1;
  }
</style>
</head>
<body>
  <main class="mailer">
    <div class="hero-photo" role="img" aria-label="Photo of a black helicopter parked on an airfield tarmac, with a smiling couple holding hands in front of it and a small jet in the distance"></div>

    <header class="brand">
      <span class="brand-mark"></span>
      <span class="brand-name">Skylark Helicopters</span>
    </header>

    <svg class="heart-art" viewBox="0 0 1000 1284" aria-hidden="true">
      <defs>
        <linearGradient id="heartFill" x1="0" y1="0" x2="0" y2="1">
          <stop offset="0" stop-color="#b0127a" stop-opacity="0"/>
          <stop offset="0.4" stop-color="#b0127a" stop-opacity="0.15"/>
          <stop offset="0.6" stop-color="#b0127a" stop-opacity="0.7"/>
          <stop offset="1" stop-color="#a0106f" stop-opacity="0.95"/>
        </linearGradient>
      </defs>
      <path class="heart-frame" d="M600,480 C560,400 440,380 360,410 C260,450 215,560 240,660 C280,810 400,900 455,1000 C560,910 740,820 830,700 C890,610 860,470 780,430 C710,400 640,420 600,480 Z" fill="url(#heartFill)" stroke="var(--pink)" stroke-width="24" stroke-linejoin="round"/>
      <path class="heart-accent" d="M729,805 C705,775 650,770 632,800 C612,840 640,890 700,970 C760,920 820,880 828,830 C835,785 760,770 729,805 Z" fill="var(--pink)"/>
      <path class="heart-spark" d="M363,355 C363,345 378,343 378,356 C378,366 367,372 363,377 C359,372 348,366 348,356 C348,343 363,345 363,355 Z" fill="var(--pink)"/>
      <path class="heart-spark" d="M394,332 C394,328 400,327 400,332 C400,336 396,338 394,340 C392,338 388,336 388,332 C388,327 394,328 394,332 Z" fill="var(--pink)"/>
      <path class="heart-spark" d="M684,288 C684,276 702,274 702,289 C702,301 689,308 684,314 C679,308 666,301 666,289 C666,274 684,276 684,288 Z" fill="var(--pink)"/>
      <path class="heart-spark" d="M701,259 C701,255 707,254 707,259 C707,263 703,265 701,267 C699,265 695,263 695,259 C695,254 701,255 701,259 Z" fill="var(--pink)"/>
    </svg>

    <section class="offer">
      <span class="offer-line">The only</span>
      <span class="offer-line"><span class="offer-highlight">Valentine’s Day</span></span>
      <span class="offer-line">Surprise,</span>
      <span class="offer-line">You’ll need</span>
      <span class="offer-sub">Enjoy the ride<br>with your valentine</span>
    </section>

    <h1 class="tour-title">Helicopter Tours</h1>
    <p class="tour-dates">AROUND VALENTINES DAY</p>
    <p class="tour-price">$169 PER PERSON</p>
  </main>
</body>
</html>
```